Design Business Card
Business Card
Design Business Card -
Creative Brief
Simple
GlowNest by Beam
Let the beautiful you reborn...
4875 Carling Ave. Suite #216 Dunmore Falls, CA 95218
bivorapelt@mailvex.net
www.glownestbybeam.net
web address is not confirmed yet; website is currently under construction. Please match coloring and concept to the logo we selected.
Appointment For:__________________ Date:_________________ Time:_________________ If you are unable to keep your appointment, please kindly give 24 hours advanced notice. $100 will be charged for cancellations/reschedules without 24 hours notice. $200 will be charged for no-shows per appointment.

```html
<!DOCTYPE html>
<html lang="en">
<head>
<meta charset="utf-8">
<title>GlowNest by Beam – Business Card</title>
<link href="https://fonts.googleapis.com/css2?family=Didact+Gothic&display=swap" rel="stylesheet">
<style>
  :root {
    --canvas-bg: #e6e6e8;
    --card-center: #b9509f;
    --card-edge: #8a2a78;
    --ink-light: #ffffff;
    --ink-soft: #f6e4f1;
    --ink-deep: #4a0f42;
    --rule: rgba(255,255,255,0.75);
  }
  * { margin: 0; padding: 0; box-sizing: border-box; }
  html, body { width: 1200px; height: 1000px; overflow: hidden; }
  body {
    background: var(--canvas-bg);
    font-family: "Didact Gothic", "Century Gothic", sans-serif;
    position: relative;
  }
  .card {
    position: absolute;
    left: 220px;
    width: 760px;
    height: 434px;
    background: radial-gradient(ellipse at 45% 45%, var(--card-center) 0%, var(--card-edge) 100%);
    color: var(--ink-light);
    box-shadow: 0 6px 18px rgba(0,0,0,0.25);
  }
  .card--front { top: 50px; }
  .card--back { top: 516px; }

  /* Front */
  .front-name {
    position: absolute;
    left: 0; right: 0; top: 110px;
    text-align: center;
    font-weight: normal;
    font-size: 100px;
    line-height: 1;
    letter-spacing: -1px;
  }
  .front-name__sub {
    display: block;
    font-size: 60px;
    margin-top: 6px;
    padding-left: 210px;
  }
  .front-tagline {
    position: absolute;
    right: 36px; top: 336px;
    font-size: 18px;
    color: var(--ink-deep);
  }

  /* Back */
  .back-name {
    position: absolute;
    left: 44px; top: 66px;
    font-weight: normal;
    font-size: 56px;
    line-height: 1;
  }
  .back-name__sub {
    display: block;
    font-size: 36px;
    padding-left: 72px;
    margin-top: 4px;
  }
  .back-address {
    position: absolute;
    left: 44px; top: 226px;
    font-size: 17px;
    line-height: 1.3;
    color: var(--ink-soft);
    font-style: normal;
  }
  .back-contact {
    position: absolute;
    left: 44px; top: 300px;
    list-style: none;
    font-size: 17px;
    line-height: 1.3;
    color: var(--ink-soft);
  }
  .appointment {
    position: absolute;
    left: 372px; top: 44px;
    width: 300px;
    font-size: 17px;
    color: var(--ink-soft);
  }
  .appointment__title { font-weight: normal; font-size: 18px; margin-bottom: 30px; }
  .appointment__field {
    display: flex;
    align-items: flex-end;
    margin-bottom: 14px;
  }
  .appointment__line {
    flex: 0 0 200px;
    border-bottom: 1px solid var(--rule);
    margin-left: 8px;
    height: 16px;
  }
  .policy {
    position: absolute;
    left: 372px; top: 312px;
    width: 330px;
    font-size: 14.5px;
    line-height: 1.25;
    color: var(--ink-soft);
  }
</style>
</head>
<body>
  <section class="card card--front" aria-label="Business card front">
    <h1 class="front-name">GlowNest<span class="front-name__sub">by Beam</span></h1>
    <p class="front-tagline">Let the beautiful you reborn...</p>
  </section>

  <section class="card card--back" aria-label="Business card back">
    <h2 class="back-name">GlowNest<span class="back-name__sub">by Beam</span></h2>
    <address class="back-address">4875 Carling Ave. Suite #216<br>Dunmore Falls, CA 95218</address>
    <ul class="back-contact">
      <li>p: 415-555-0142</li>
      <li>f: 415-555-0187</li>
      <li>e: bivorapelt@mailvex.net</li>
      <li>www.glownestbybeam.net</li>
    </ul>

    <div class="appointment">
      <h3 class="appointment__title">Appointment</h3>
      <div class="appointment__field"><span>For:</span><span class="appointment__line"></span></div>
      <div class="appointment__field"><span>Date:</span><span class="appointment__line"></span></div>
      <div class="appointment__field"><span>Time:</span><span class="appointment__line"></span></div>
    </div>

    <p class="policy">If you are unable to keep your appointment, please kindly give 24 hours advanced notice. $100 will be charged for cancellations/reschedules without 24 hours notice. $200 will be charged for no-shows per appointment.</p>
  </section>
</body>
</html>
```